Education Foundation Needs a Flyer for an Awareness/Fundraising Event

We need a flyer design for our Education Celebration that is held each year to commemorate Lone Prairie Learning Week.

This event provides an excellent opportunity for the community to come together to celebrate the education of our children and support the Brisbane Ridge Unified School District. All twelve schools in the district will have tabletop displays highlighting some of their activities during the year. Teachers will also have grant displays to spotlight the innovative classroom projects they implemented due to funding provided by the Brisbane Ridge Education Foundation.

The evening will also include entertainment provided by BRUSD school choirs. The event concludes with drawing for prices, and a raffle drawing.

Listed below are the details that need to be included in the flyer. I have also included our logo that must be used. I also included some photos from past celebrations that may or may not be helpful.

Please join the Brisbane Ridge Education Foundation as we celebrate BRUSD and its students, educational programs, and schools.

Thursday, March 26, 2015
5:00 p.m. – 8:00 p.m.
Brisbane Ridge High School

Students: Please sign up to be entered in a drawing for Kumora Pocket.
Adults: Please sign up to be entered in a drawing for a $50 Shopwell Gift Card.

Raffle Prizes
TELVANA 50" Class 1080p LED Smart HDTV
Zentra Play Console w/ Motionpad
Donations of $2 each or 3 for $5, or 7 for $10
*Tickets are available at the BRUSD Administration Building/ Communications and at the schools. (You must be present to win.)

Prizes Galore!
• Campus with the highest percentage of adult attendance will win $300 + the Traveling
Trophy for one year.
• Campus with the 2nd highest percentage of adult attendance will win $150.
• Additional drawings for Teacher, Principal/ Asst. Principal, and District Personnel will be held.

Your Choice – Your Prize
Drawings

7" Orvel NEBULA Pad 4
Brightline Streamstick
Brewmont Classic B30 Single Serve
External Hard Drive
Brewmont 3.0 B700 Coffee Brewing System w/ Carafe
Brightline Streamstick
Cotton Candy Maker
*For your donation of $1.00 per ticket, you may place your ticket(s) in one or all of the baskets. It’s your choice. (You must be present to win.)

Food!
Hot Dogs $1.00
Corn Dogs $0.75
Chips $0.50
Drinks $0.75
Cookies $0.75
Baskets - $2.50 (Hot Dog or Corn Dog, Chips, Drink, Cookie)

For more information, please call 555-318-2946.

```html
<!DOCTYPE html>
<html lang="en">
<head>
<meta charset="utf-8">
<title>Brisbane Ridge Education Foundation – Education Celebration</title>
<link rel="stylesheet" href="https://fonts.googleapis.com/css2?family=Oswald:wght@500;600&family=Roboto+Condensed:wght@400;700&family=Open+Sans:wght@400;600&display=swap">
<style>
  :root {
    --blue: #1f3c8f;
    --blue-deep: #17307a;
    --gold: #f3c431;
    --red: #8e1b1f;
    --ink: #1d1d1d;
    --paper: #f4f6f8;
    --paper-edge: #e2e6ea;
    --grey-panel: #a9abae;
    --photo-a: #b9a48a;
    --photo-b: #6b5a4c;
  }
  * { margin: 0; padding: 0; box-sizing: border-box; }
  html, body { width: 926px; height: 1200px; overflow: hidden; background: #fff; }
  .flyer {
    position: relative; width: 926px; height: 1200px; overflow: hidden;
    background: linear-gradient(180deg, var(--paper) 0%, #ffffff 45%, var(--paper-edge) 100%);
    font-family: "Open Sans", Arial, sans-serif; color: var(--ink);
  }
  .hero-photo {
    position: absolute; left: 0; top: 0; width: 926px; height: 463px;
    background: linear-gradient(135deg, #c9b79c 0%, var(--photo-a) 35%, #8d7a68 70%, var(--photo-b) 100%);
  }
  .banner {
    position: absolute; left: 0; top: 463px; width: 926px; height: 123px;
    background: var(--blue); text-align: center; color: #fff;
  }
  .banner-title {
    font-family: "Oswald", sans-serif; font-weight: 600; color: var(--gold);
    font-size: 36px; letter-spacing: 0.5px; margin-top: 14px; line-height: 44px;
  }
  .banner-sub { font-size: 17px; line-height: 24px; margin-top: 2px; }
  .banner-details {
    font-family: "Roboto Condensed", sans-serif; font-size: 16px; line-height: 24px; margin-top: 4px;
  }
  .col { position: absolute; top: 586px; }
  .col-left { left: 33px; width: 412px; padding-top: 24px; }
  .col-right { left: 480px; width: 420px; padding-top: 26px; }
  .section-head {
    font-family: "Roboto Condensed", sans-serif; font-weight: 700; color: var(--blue);
    font-size: 22px; line-height: 30px;
  }
  .body-text { font-size: 15px; line-height: 22px; }
  .note { font-size: 13px; line-height: 18px; }
  .spaced { margin-top: 20px; }
  .prize-list { list-style: none; font-size: 15px; line-height: 22px; text-align: justify; }
  .prize-list li { position: relative; padding-left: 16px; }
  .prize-list li::before { content: "•"; position: absolute; left: 0; }
  .audience { margin-top: 22px; font-size: 13px; line-height: 18px; }
  .audience-label { color: var(--red); font-weight: 600; display: block; }
  .choice-title {
    font-family: "Oswald", sans-serif; font-weight: 500; color: var(--red);
    font-size: 34px; line-height: 40px; margin-bottom: 6px;
  }
  .footer-art { position: absolute; left: 0; top: 0; }
  .logo { position: absolute; left: 128px; top: 1090px; width: 90px; text-align: center; }
  .logo-name {
    font-family: "Roboto Condensed", sans-serif; font-weight: 700; color: var(--blue);
    font-size: 18px; line-height: 20px; margin-top: 4px;
  }
  .site { position: absolute; left: 33px; top: 1166px; font-size: 13px; color: #333; }
  .call {
    position: absolute; left: 380px; top: 1146px; width: 520px; text-align: right;
    color: #fff; font-family: "Roboto Condensed", sans-serif; font-weight: 700; font-size: 22px;
    line-height: 40px;
  }
  .call-number { font-family: "Oswald", sans-serif; font-weight: 600; color: var(--gold); font-size: 34px; vertical-align: -3px; }
</style>
</head>
<body>
<div class="flyer">
  <div class="hero-photo" role="img" aria-label="Collage photo of families, students and staff smiling together at a past school district celebration in a busy cafeteria"></div>

  <header class="banner">
    <h1 class="banner-title">JOIN THE BRISBANE RIDGE EDUCATION FOUNDATION</h1>
    <p class="banner-sub">as we celebrate BRUSD and its students, educational programs, and schools</p>
    <p class="banner-details">Thursday, March 26, 2015 &nbsp;|&nbsp; 5:00 p.m. – 8:00 p.m. &nbsp;|&nbsp; Brisbane Ridge High School</p>
  </header>

  <section class="col col-left">
    <h2 class="section-head">Raffle Prizes</h2>
    <p class="body-text">TELVANA 50" Class 1080p LED Smart HDTV<br>Zentra Play Console w/ Motionpad<br>Donations of $2 each or 3 for $5, or 7 for $10</p>
    <p class="note">*Tickets are available at the BRUSD Administration Building/ Communications and at the schools. (You must be present to win.)</p>

    <h2 class="section-head spaced">Prizes Galore!</h2>
    <ul class="prize-list">
      <li>Campus with the highest percentage of adult attendance will win $300 + the Traveling Trophy for one year.</li>
      <li>Campus with the 2nd highest percentage of adult attendance will win $150.</li>
      <li>Additional drawings for Teacher, Principal/ Asst. Principal, and District Personnel will be held.</li>
    </ul>

    <p class="audience"><span class="audience-label">Students:</span>Please sign up to be entered in a drawing for Kumora Pocket.</p>
    <p class="note"><span class="audience-label">Adults:</span>Please sign up to be entered in a drawing for a $50 Shopwell Gift Card.</p>
  </section>

  <section class="col col-right">
    <h2 class="choice-title">YOUR CHOICE – YOUR PRIZE</h2>
    <h3 class="section-head">Drawings</h3>
    <p class="body-text">7" Orvel NEBULA Pad 4<br>Brightline Streamstick<br>Brewmont Classic B30 Single Serve<br>External Hard Drive<br>Brewmont 3.0 B700 Coffee Brewing System w/ Carafe<br>Brightline Streamstick<br>Cotton Candy Maker</p>
    <p class="note">*For your donation of $1.00 per ticket, you may place your ticket(s) in one or all of the baskets. It’s your choice. (You must be present to win.)</p>

    <h3 class="section-head spaced">Food!</h3>
    <p class="body-text">Hot Dogs $1.00<br>Corn Dogs $0.75<br>Chips $0.50<br>Drinks $0.75<br>Cookies $0.75<br>Baskets - $2.50 (Hot Dog or Corn Dog, Chips, Drink, Cookie)</p>
  </section>

  <svg class="footer-art" width="926" height="1200" viewBox="0 0 926 1200" aria-hidden="true">
    <polygon points="0,1077 300,1077 340,1200 0,1200" fill="var(--grey-panel)" opacity="0.55"/>
    <polygon points="300,1131 926,1131 926,1200 322,1200" fill="var(--blue)"/>
    <circle cx="173" cy="1108" r="16" fill="var(--blue)"/>
  </svg>

  <div class="logo" style="top:1126px;"><p class="logo-name">BREF</p></div>
  <p class="site">www.brisbaneridgeedfoundation.org</p>
  <p class="call">For more information please call: <span class="call-number">555-318-2946</span></p>
</div>
</body>
</html>
```